Business Card Design

Marla Quenby
Artist of Contemporary/Modern/Representational Art
Contact: 0429175348
Please include my web site (thanks)! http://www.artloft583.com.au/marla-quenby
And
Email: marlaquenby@vexmail.com

Target Market(s)

Modern professional People who know what they like in modern contemporary art and have the means to purchase it.

Industry/Entity Type

Business

Contact Information for Business Card

Marla Quenby
Contact: 0429175348

Font styles to use
Sans Serif

Requirements
Must have
• Simplicity & to the point
Keep the font modern/ contemporary
Nice to have
• A portrait of me and one piece of work on the business card (one on each side).
Should not have
• I'm not into butterflies.
No feminine style swirls
Nor I like swirls that look like tatoos

```html
<!DOCTYPE html>
<html lang="en">
<head>
<meta charset="utf-8">
<title>Marla Quenby — Business Card</title>
<link rel="stylesheet" href="https://fonts.googleapis.com/css2?family=Philosopher:ital,wght@0,400;0,700;1,400&display=swap">
<style>
  :root {
    --stage: #2b2b2d;
    --card-black: #0c0c0c;
    --ink-white: #f4f4f4;
    --ink-soft: #d8d8d8;
    --sky: #5fb6d3;
    --sky-light: #bfe4ee;
    --park-green: #5c9a3a;
    --city-grey: #8a8f96;
    --band-black: #050505;
  }
  * { margin: 0; padding: 0; box-sizing: border-box; }
  html, body {
    width: 1200px; height: 850px; overflow: hidden;
    background: var(--stage);
    font-family: "Philosopher", "Trebuchet MS", sans-serif;
  }
  .stage {
    width: 1200px; height: 850px;
    display: flex; align-items: center; justify-content: center; gap: 50px;
  }
  .card {
    position: relative;
    width: 540px; height: 330px;
    overflow: hidden;
    box-shadow: 0 10px 30px rgba(0,0,0,.45);
  }
  /* Back: artwork side */
  .card-back { background: var(--card-black); }
  .artwork {
    position: absolute; inset: 0 0 34px 0;
    background:
      linear-gradient(180deg, var(--sky) 0%, var(--sky-light) 28%, var(--city-grey) 45%, var(--park-green) 75%, #3f6f2c 100%);
  }
  .back-band {
    position: absolute; left: 0; right: 0; bottom: 0; height: 34px;
    background: var(--band-black);
    color: var(--ink-white);
    font-size: 15px; line-height: 34px; padding-left: 40px;
  }
  /* Front: contact side */
  .card-front { background: var(--card-black); color: var(--ink-white); }
  .portrait {
    position: absolute; left: 28px; top: 96px;
    width: 62px; height: 62px; border-radius: 7px;
    background: linear-gradient(160deg, #b9b9b9, #6e6e6e);
  }
  .name {
    position: absolute; left: 100px; top: 58px;
    font-size: 60px; font-weight: 700; letter-spacing: .5px; line-height: 1;
  }
  .role {
    position: absolute; left: 102px; top: 132px;
    font-size: 12.5px; color: var(--ink-soft); letter-spacing: .3px;
  }
  .contact {
    position: absolute; right: 40px; bottom: 42px;
    text-align: right; font-size: 13.5px; line-height: 1.45; color: var(--ink-soft);
  }
  .contact strong { color: var(--ink-white); font-weight: 700; }
  .contact em { font-style: italic; }
</style>
</head>
<body>
  <main class="stage">
    <section class="card card-back">
      <div class="artwork" role="img" aria-label="Painting of a colourful city skyline curving around a river and parkland"></div>
      <p class="back-band">view more of my artwork</p>
    </section>

    <section class="card card-front">
      <div class="portrait" role="img" aria-label="Portrait photograph of the artist"></div>
      <h1 class="name">Marla Quenby</h1>
      <p class="role">Artist of Contemporary/Modern/Representational Art</p>
      <address class="contact">
        Mob <strong>0429175348</strong><br>
        Email <strong>marlaquenby@vexmail.com</strong><br>
        view my artwork at www.artloft583.com.au/<em>marla-quenby</em>
      </address>
    </section>
  </main>
</body>
</html>
```